Premium Business Cards

Hi
I need 5 premium business cards for my clients, and need very urgent.
Requirements:
1. Simple
2. Professional
3. Black /Dark
Our client product is Premium Vellmont Clothing, for privacy reason, we are unable to upload their logo, sorry.

Target Market(s)

Top level customer, aged 35 to 60 European.

Industry/Entity Type

Business

Font styles to use
Script

Requirements
Must have
• The business cards must in dark theme, our logo color is metal yellow and white gold.
Size 90mmx55mm double sided.
Should not have
• Don't like fancy color or bright color.

```html
<!DOCTYPE html>
<html lang="en">
<head>
<meta charset="utf-8">
<title>Vellmont Business Card</title>
<link rel="stylesheet" href="https://fonts.googleapis.com/css2?family=Source+Sans+3:ital,wght@0,400;0,600;1,700&display=swap">
<style>
  :root {
    --paper: #ffffff;
    --card-black: #000000;
    --lapel-grey: #272727;
    --metal-gold: #a7843f;
    --text-grey: #9b9b9b;
    --white-gold: #ecebe6;
  }
  html, body {
    margin: 0;
    width: 1200px;
    height: 918px;
    overflow: hidden;
    background: var(--paper);
  }
  .sheet {
    width: 1382px;
    height: 1050px;
    transform: scale(0.8683, 0.8743);
    transform-origin: 0 0;
  }
  .sheet svg { display: block; }
  .card-body { fill: var(--card-black); }
  .lapel { fill: var(--lapel-grey); }
  .lapel-edge { fill: none; stroke: var(--metal-gold); stroke-width: 6; stroke-linejoin: miter; }
  .gold-trim { fill: var(--metal-gold); }
  .brand-name {
    font-family: "Source Sans 3", sans-serif;
    font-weight: 400;
    fill: var(--metal-gold);
  }
  .brand-tagline {
    font-family: "Source Sans 3", sans-serif;
    font-weight: 400;
    fill: var(--white-gold);
  }
  .office-heading {
    font-family: "Source Sans 3", sans-serif;
    font-weight: 700;
    font-style: italic;
    font-size: 40px;
    fill: var(--text-grey);
  }
  .contact-line {
    font-family: "Source Sans 3", sans-serif;
    font-weight: 400;
    font-size: 36px;
    fill: var(--text-grey);
  }
</style>
</head>
<body>
<div class="sheet">
  <svg width="1382" height="1050" viewBox="0 0 1382 1050" xmlns="http://www.w3.org/2000/svg">
    <!-- Back side: contact details -->
    <g class="card-back">
      <polygon class="card-body" points="240,88 657,88 657,972 116,972 116,432"/>
      <polygon class="lapel" points="240,88 426,88 285,232 229,226 246,294 116,432"/>
      <polyline class="lapel-edge" points="426,88 285,232 229,226 246,294 116,432"/>
      <polygon class="gold-trim" points="116,432 132,953 657,972 116,972"/>

      <text class="brand-name" x="628" y="200" text-anchor="end" font-size="70">Vellmont</text>
      <text class="brand-tagline" x="623" y="228" text-anchor="end" font-size="17" letter-spacing="4">Premium Clothing</text>

      <text class="office-heading" x="608" y="530" text-anchor="end">Office Address</text>
      <text class="contact-line" x="615" text-anchor="end">
        <tspan x="615" y="620">4410 Aspen Row</tspan>
        <tspan x="615" y="669">Colorado 80211</tspan>
        <tspan x="615" y="718">USA</tspan>
        <tspan x="615" y="767">+1 303 555 0142</tspan>
        <tspan x="615" y="816">+1 303 555 0187</tspan>
        <tspan x="615" y="865">www.vellmont.com</tspan>
        <tspan x="615" y="914">hello@vellmont.com</tspan>
      </text>
    </g>

    <!-- Front side: brand -->
    <g class="card-front">
      <polygon class="card-body" points="733,88 1150,88 1274,432 1274,972 733,972"/>
      <text class="brand-name" x="1003" y="548" text-anchor="middle" font-size="140">Vellmont</text>
      <text class="brand-tagline" x="1000" y="603" text-anchor="middle" font-size="34" letter-spacing="8">Premium Clothing</text>
    </g>
  </svg>
</div>
</body>
</html>
```